Website for harborlyn mobile detailing.

Need a homepage, pages for: car and truck detailing, boat detailing, airplane detailing, about us, contact us. I have the domain name through quillnest so I will need the design uploaded on my domain. Also hoping to link other domains to this page.I would like to see the logo more pronounced. I would like to see a large phone number link to call my business. The layout looks nice but the pics need to depict car washing and waxing not car mechanics. i would like the colors of the webpage to incorporate the colors found in the logo in some way. I would like links to social media pages
Updates

Need extra days to review

Target Market(s)

Local customers in Vero Beach, Florida.

Number of Pages Required

5+ page

Colors

Designer to choose colors to be used in the design.

Requirements
Must have
• Easy to navigate, attractive pages with pictures and logo, professional looking. must have my phone number and logo very prevalent and links to call or go to home page. I would like links to my social media accounts on the home page.
Nice to have
• Easy to navigate, attractive pages with pictures and logo, professional looking.

```html
<!DOCTYPE html>
<html lang="en">
<head>
<meta charset="utf-8">
<title>Harborlyn Mobile Detailing</title>
<link rel="stylesheet" href="https://fonts.googleapis.com/css2?family=Open+Sans:wght@400;600;700;800&family=Ubuntu:wght@500;700&display=swap">
<style>
  :root {
    --red: #e8262c;
    --red-deep: #d81f25;
    --navy: #1b2a6b;
    --blue: #0aa3e0;
    --ink: #222222;
    --text: #555555;
    --band: #ececec;
    --rule: #d6d6d6;
    --field: #b9b9b9;
    --white: #ffffff;
  }
  * { margin: 0; padding: 0; box-sizing: border-box; }
  html, body { width: 1200px; height: 2560px; overflow: hidden; }
  body { position: relative; font-family: "Open Sans", sans-serif; color: var(--text); background: var(--white); }
  .abs { position: absolute; }

  /* hero */
  .hero-photo { left: 0; top: 0; width: 1200px; height: 533px;
    background:
      radial-gradient(ellipse 150px 230px at 560px 300px, rgba(30,30,34,0.95) 0%, rgba(40,40,44,0.7) 45%, rgba(60,60,64,0) 100%),
      linear-gradient(172deg, rgba(255,255,255,0) 55%, rgba(70,60,50,0.55) 72%, rgba(40,36,32,0.75) 100%),
      radial-gradient(ellipse 380px 260px at 930px 150px, #f6f6f6 0%, #dedfe1 60%, rgba(220,220,222,0) 100%),
      linear-gradient(90deg, #f7f7f7 0%, #e9eaec 22%, #c9ccd0 38%, #aeb3b8 50%, #d6d8db 68%, #eeeeee 100%); }
  .brand { left: 162px; top: 16px; display: flex; align-items: center; gap: 10px; }
  .brand-dot { width: 40px; height: 40px; border-radius: 50%; background: var(--navy); }
  .brand-name { font-family: "Ubuntu", sans-serif; font-weight: 700; font-size: 24px; line-height: 1.02; color: var(--navy); }
  .brand-phone { left: 178px; top: 70px; font-family: "Ubuntu", sans-serif; font-weight: 700; font-size: 24px; letter-spacing: 1.5px; color: var(--red); text-decoration: none; display: flex; align-items: center; gap: 8px; }
  .nav a { position: absolute; top: 28px; transform: translateX(-50%); white-space: nowrap; font-size: 12px; font-weight: 700; color: var(--navy); text-decoration: none; }
  .nav a.active { color: var(--red); }
  .nav-marker { left: 617px; top: 0; width: 40px; height: 4px; background: var(--red); }
  .headline { left: 0; width: 1200px; top: 488px; text-align: center; font-weight: 800; font-size: 45px; color: var(--red); letter-spacing: 0.3px; }
  .intro-band { left: 0; top: 533px; width: 1200px; height: 145px; background: var(--red); }
  .intro-text { left: 188px; top: 574px; width: 824px; text-align: center; color: var(--white); font-size: 11.5px; line-height: 20px; font-weight: 600; }

  /* about */
  .about-title { left: 162px; top: 738px; font-family: "Ubuntu", sans-serif; font-weight: 700; font-size: 26px; line-height: 40px; letter-spacing: 1.5px; color: var(--ink); }
  .about-rule { left: 162px; top: 879px; width: 231px; height: 2px; background: var(--rule); }
  .about-rule::before { content: ""; position: absolute; left: 0; top: -1px; width: 94px; height: 4px; background: var(--red); }
  .about-copy { left: 432px; top: 744px; width: 600px; font-size: 11px; line-height: 19px; }
  .about-copy p + p { margin-top: 20px; }
  .features { left: 432px; top: 870px; display: flex; list-style: none; font-size: 11px; }
  .features li { position: relative; padding-left: 13px; }
  .features li::before { content: ""; position: absolute; left: 0; top: 6px; width: 6px; height: 6px; background: var(--red); }
  .features li:nth-child(1) { width: 106px; }
  .features li:nth-child(2) { width: 71px; }

  /* services */
  .services-band { left: 0; top: 987px; width: 1200px; height: 179px; background: var(--band); }
  .services-title { left: 0; width: 1200px; top: 1024px; text-align: center; font-family: "Ubuntu", sans-serif; font-weight: 700; font-size: 29px; letter-spacing: 3px; color: var(--ink); }
  .services-rule { left: 505px; top: 1082px; width: 191px; height: 1px; background: var(--rule); }
  .services-rule::before { content: ""; position: absolute; left: 62px; top: -1px; width: 65px; height: 4px; background: var(--red); }
  .tabs a { position: absolute; top: 1112px; transform: translateX(-50%); font-size: 16px; font-weight: 700; letter-spacing: 1.5px; color: #8b8b8b; text-decoration: none; }
  .tabs a.active { color: var(--red); }
  .tab-pointer { left: 591px; top: 1136px; }
  .band-notch { left: 584px; top: 1165px; }
  .services-stage { left: 0; top: 1166px; width: 1200px; height: 638px;
    background:
      radial-gradient(ellipse 520px 300px at 560px 300px, rgba(120,100,60,0.55) 0%, rgba(70,60,40,0.35) 50%, rgba(0,0,0,0) 100%),
      radial-gradient(ellipse 300px 200px at 1000px 520px, rgba(110,90,40,0.5) 0%, rgba(0,0,0,0) 100%),
      linear-gradient(180deg, #2a2822 0%, #121210 60%, #050505 100%); }
  .tile { position: absolute; }
  .photo.headlight { background:
      radial-gradient(ellipse 140px 100px at 390px 150px, #2a7fd0 0%, rgba(42,127,208,0) 100%),
      linear-gradient(160deg, #c9d8e6 0%, #aebfcf 35%, #7f90a0 60%, #5b6f55 100%); }
  .photo.polish { background:
      radial-gradient(ellipse 110px 90px at 90px 110px, #6d5a3a 0%, rgba(109,90,58,0) 100%),
      radial-gradient(ellipse 90px 120px at 200px 210px, #b42a2c 0%, rgba(180,42,44,0) 100%),
      linear-gradient(135deg, #f4f4f4 0%, #e3e3e3 50%, #cfcfcf 100%); }
  .photo.rear { background:
      radial-gradient(ellipse 70px 40px at 80px 110px, #a3202a 0%, rgba(163,32,42,0) 100%),
      radial-gradient(ellipse 40px 60px at 220px 100px, #c33030 0%, rgba(195,51,48,0) 100%),
      linear-gradient(150deg, #2d2f33 0%, #8c8e92 30%, #e4e4e4 60%, #f2f2f2 100%); }
  .card { padding: 17px; color: var(--white); }
  .card.blue { background: var(--blue); }
  .card.red { background: var(--red-deep); }
  .card-inner { width: 100%; height: 100%; border: 1px solid rgba(255,255,255,0.85); padding: 20px 14px 0; }
  .card h3 { font-size: 15px; font-weight: 700; letter-spacing: 1px; line-height: 22px; margin-bottom: 8px; }
  .card p { font-size: 10.5px; line-height: 16px; font-weight: 600; }
  .card a { display: inline-block; margin-top: 10px; font-size: 10.5px; font-weight: 800; color: var(--white); text-decoration: none; }

  /* map */
  .map { left: 0; top: 1804px; width: 1200px; height: 369px;
    background:
      radial-gradient(ellipse 300px 140px at 700px 200px, #f3f3f3 0%, rgba(243,243,243,0) 100%),
      radial-gradient(ellipse 260px 160px at 1000px 120px, #dcdcdc 0%, rgba(220,220,220,0) 100%),
      linear-gradient(180deg, #ececec 0%, #e4e4e4 100%); }
  .map-toggle { top: 1812px; left: 1108px; display: flex; background: var(--white); box-shadow: 0 1px 3px rgba(0,0,0,0.3); font-size: 10px; color: #222; }
  .map-toggle span { padding: 4px 6px; }
  .map-toggle span + span { border-left: 1px solid #ddd; color: #555; }
  .map-pan { left: 14px; top: 1826px; }
  .map-zoom { left: 30px; top: 1935px; width: 16px; height: 200px; }
  .map-zoom::before { content: ""; position: absolute; left: 7px; top: 10px; width: 2px; height: 180px; background: #c8c8c8; }
  .map-zoom span { position: absolute; left: 0; width: 16px; height: 16px; background: var(--white); border: 1px solid #bbb; font-size: 12px; line-height: 13px; text-align: center; color: #555; }
  .map-card { left: 239px; top: 1936px; width: 249px; height: 147px; background: var(--white); box-shadow: 0 1px 4px rgba(0,0,0,0.25); padding: 18px 12px; font-size: 11px; line-height: 16px; color: #444; }
  .map-card .row { display: flex; align-items: center; gap: 8px; margin-top: 10px; }

  /* footer */
  .footer { left: 0; top: 2173px; width: 1200px; height: 387px;
    background:
      radial-gradient(ellipse 200px 260px at 420px 120px, rgba(70,70,70,0.6) 0%, rgba(0,0,0,0) 100%),
      linear-gradient(120deg, #262626 0%, #141414 60%, #1d1d1d 100%); }
  .footer-title { left: 162px; top: 2200px; font-family: "Ubuntu", sans-serif; font-weight: 700; font-size: 25px; color: var(--white); }
  .footer-sub { left: 162px; top: 2240px; font-size: 11px; color: #aaaaaa; }
  .footer-rule { left: 162px; top: 2268px; width: 98px; height: 3px; background: var(--red); }
  .social { left: 162px; top: 2300px; display: flex; gap: 8px; }
  .social a { width: 37px; height: 37px; border-radius: 50%; background: #8f8f8f; display: block; }
  .field { position: absolute; background: var(--field); border-radius: 2px; font-size: 11px; color: #222; padding: 9px 12px; }
  .submit { left: 589px; top: 2414px; width: 177px; height: 46px; border: 2px solid var(--red); color: var(--red); font-size: 14px; text-align: center; line-height: 42px; letter-spacing: 1px; }
  .copyright { left: 0; width: 1200px; top: 2519px; text-align: center; font-size: 10px; color: #9a9a9a; }
  .copyright b { color: var(--red); font-weight: 700; }
</style>
</head>
<body>

<!-- hero -->
<div class="abs hero-photo" role="img" aria-label="Detailer pressure-washing the hull of a white boat at the marina"></div>
<div class="abs brand"><span class="brand-dot"></span><span class="brand-name">Harborlyn<br>Mobile Detailing</span></div>
<a class="abs brand-phone" href="tel:5550182746">
  <svg width="20" height="20" viewBox="0 0 20 20"><path d="M5 2l3 4-1.6 1.8c1 2.2 2.6 3.8 4.8 4.8L13 11l4 3-1.4 3C9 16.6 3.4 11 3 4.4z" fill="var(--red)"/></svg>
  555-018-2746
</a>
<div class="abs nav-marker"></div>
<nav class="nav">
  <a class="active" href="#" style="left:637px">HOME</a>
  <a href="#" style="left:722px">ABOUT US</a>
  <a href="#" style="left:816px">SERVICES</a>
  <a href="#" style="left:905px">CLIENTS</a>
  <a href="#" style="left:1000px">CONTACT US</a>
</nav>
<div class="abs intro-band"></div>
<h1 class="abs headline">FROM 30 YEARS WE PROVIDE SERVICE</h1>
<p class="abs intro-text">Lorem ipsum dolor sit amet, consectetur adipiscing elit, sed do eiusmod tempor incididunt ut labore et dolore magna aliqua. Ut enim ad minim veniam, quis nostrud exercitation ullamco laboris nisi ut aliquip ex ea commodo consequat. Duis aute irure dolor in reprehenderit in voluptate velit esse cillum dolore eu fugiat nulla pariatur. Excepteur sint occaecat cupidatat non proident, sunt in culpa qui officia deserunt mollit anim id est laborum.</p>

<!-- about -->
<h2 class="abs about-title">ABOUT HARBOR-<br>LYN MOBILE<br>DETAILING</h2>
<div class="abs about-rule"></div>
<div class="abs about-copy">
  <p>Lorem ipsum dolor sit amet, consectetur adipiscing elit, sed do eiusmod tempor incididunt ut labore et dolore magna aliqua. Ut enim ad minim veniam, quis nostrud exercitation.</p>
  <p>Duis aute irure dolor in reprehenderit in voluptate velit esse cillum dolore eu fugiat nulla pariatur. Excepteur sint occaecat cupidatat non proident, sunt in culpa qui officia deserunt mollit anim id est laborum.</p>
</div>
<ul class="abs features"><li>Wash</li><li>Wax</li><li>Degrease</li></ul>

<!-- services -->
<div class="abs services-band"></div>
<h2 class="abs services-title">SERVICES</h2>
<div class="abs services-rule"></div>
<div class="tabs">
  <a href="#" style="left:527px">BOAT</a>
  <a class="active" href="#" style="left:597px">CAR</a>
  <a href="#" style="left:691px">AIRPLANE</a>
</div>
<svg class="abs tab-pointer" width="12" height="7" viewBox="0 0 12 7"><path d="M0 0h12L6 7z" fill="var(--red)"/></svg>
<div class="abs services-stage" role="img" aria-label="Dark close-up of a freshly washed car body"></div>
<svg class="abs band-notch" width="28" height="14" viewBox="0 0 28 14"><path d="M0 0h28L14 14z" fill="var(--band)"/></svg>

<div class="tile card blue" style="left:160px;top:1239px;width:280px;height:178px">
  <div class="card-inner"><h3>CAR WAX</h3><p>Lorem ipsum dolor sit amet, consectetur adipiscing elit, sed do eiusmod tempor incididunt ut labore et dolore magna</p><a href="#">MORE</a></div>
</div>
<div class="tile photo headlight" style="left:473px;top:1239px;width:567px;height:280px" role="img" aria-label="Hand wiping a car headlight with a blue microfibre cloth"></div>
<div class="tile photo polish" style="left:160px;top:1451px;width:280px;height:282px" role="img" aria-label="Rotary polisher buffing white car paint"></div>
<div class="tile photo rear" style="left:473px;top:1553px;width:280px;height:180px" role="img" aria-label="Rear light of a white car with a detailer crouching nearby"></div>
<div class="tile card red" style="left:785px;top:1553px;width:255px;height:180px">
  <div class="card-inner" style="padding:14px 12px 0"><h3>CAR DEGREASE</h3><p>Lorem ipsum dolor sit amet, consectetur adipiscing elit, sed do eiusmod tempor incididunt ut labore</p><a href="#" style="margin-top:8px">MORE</a></div>
</div>

<!-- map -->
<div class="abs map" role="img" aria-label="Street map showing the business location"></div>
<div class="abs map-toggle"><span>Map</span><span>Satellite</span></div>
<svg class="abs map-pan" width="46" height="46" viewBox="0 0 46 46"><circle cx="23" cy="23" r="21" fill="#fff" stroke="#bbb"/><path d="M23 8l-4 5h8zM23 38l-4-5h8zM8 23l5-4v8zM38 23l-5-4v8z" fill="#666"/></svg>
<div class="abs map-zoom"><span style="top:0">+</span><span style="bottom:0">−</span></div>
<div class="abs map-card">
  <div>Address :</div>
  <div>Lorem Ipsum Dolor Sit Amet<br>Consectetur</div>
  <div class="row">
    <svg width="12" height="12" viewBox="0 0 12 12"><circle cx="6" cy="6" r="5.5" fill="none" stroke="var(--red)"/><path d="M4 3.2l1 1.2-.6.8c.5 1 1.2 1.7 2.2 2.2l.8-.6 1.2 1-.6 1c-2.6-.2-4.6-2.2-4.8-4.8z" fill="var(--red)"/></svg>
    <span>+012 3456 7890</span>
  </div>
  <div class="row" style="margin-top:4px">
    <svg width="12" height="10" viewBox="0 0 12 10"><rect x="0.5" y="0.5" width="11" height="9" fill="none" stroke="var(--red)"/><path d="M0.5 0.5L6 5.5l5.5-5" fill="none" stroke="var(--red)"/></svg>
    <span>info@harborlynmobiledetailing.com</span>
  </div>
</div>

<!-- footer -->
<div class="abs footer" role="img" aria-label="Detailer at work in a dim garage"></div>
<h2 class="abs footer-title">Contacto</h2>
<div class="abs footer-sub">Compañía Marítima Ribera.</div>
<div class="abs footer-rule"></div>
<div class="abs social">
  <a href="#" aria-label="Social network 1"></a>
  <a href="#" aria-label="Social network 2"></a>
  <a href="#" aria-label="Social network 3"></a>
  <a href="#" aria-label="Social network 4"></a>
  <a href="#" aria-label="Social network 5"></a>
</div>
<div class="field" style="left:589px;top:2219px;width:217px;height:39px">Su Nombre</div>
<div class="field" style="left:823px;top:2219px;width:217px;height:39px">Email</div>
<div class="field" style="left:589px;top:2272px;width:451px;height:39px">Asunto</div>
<div class="field" style="left:589px;top:2323px;width:451px;height:79px">Mensaje</div>
<div class="abs submit">SUBMIT</div>
<p class="abs copyright">Copyrights©2018 <b>HARBORLYN MOBILE DETAILING</b> Allrights are reserved</p>

</body>
</html>
```